Inspiring Poster for Company Staff Room

What we need:
We want an awesome design to create a poster that will be plaque mounted in our staff room. We just went through a very motivating workshop to discover our "WHY" as a company...basically, to define the reason we are in business, and to define what motivates us to come to work every day. The poster must be motivating but really resonate with our team…we are not looking for a “typical” motivational poster that we can purchase off Brindleway!

Who we are:
We are a property management company, a team of 20 that is passionate about our investors, and residents who rent from us, but more importantly, we love helping people and making a difference in our industry. We are proud and work hard for every single 5 star Quorvix review we achieve.

Information for you:
We have included a mock up of the poster, which words we want, and the placement of them (in a general sense) but we need a designer to really bring this together in an inspiring poster that represents our company’s culture, feel, and fit. We have also included a logo file, as well as examples of our business cards, letterhead and thank you card already designed.
Here are the parameters:

(1) Poster size: 24” x 36”
(2) Full colour
(3) Must incorporate our company logo
(4) Must incorporate the following words:

Why do I come to work?

“To feel fulfilled by empathizing, educating and empowering our clients and co-workers so that we can build strong, impactful relationships”

Own the outcome

(5) Please see our website at www.larkmoorpm.example to get a feel for our company culture and for a better idea of our current company graphics

Target Market(s)

Our staff. Will not be seen by our clients

Industry/Entity Type

Real Estate

Font styles to use
Serif
Sans Serif

Requirements
Should not have
• Would not want this to be too "busy." if you can picture it, the poster will be mounted on the wall as soon as someone enters the room. The idea is to remind them each day why they come to work.

```html
<!DOCTYPE html>
<html lang="en">
<head>
<meta charset="utf-8">
<title>Larkmoor Property Management – Why do I come to work?</title>
<link rel="stylesheet" href="https://fonts.googleapis.com/css2?family=Inter:wght@600;700;800&display=swap">
<style>
  :root {
    --purple: #8b2a8c;
    --orange: #f58025;
    --blue: #234e9f;
    --pink: #d2479a;
    --charcoal: #404040;
    --headline-pink: #f288b8;
    --white: #ffffff;
    --shadow: rgba(80, 20, 70, 0.55);
  }
  html, body {
    margin: 0;
    padding: 0;
    overflow: hidden;
    background: #ffffff;
  }
  .poster {
    position: relative;
    width: 800px;
    height: 1200px;
    overflow: hidden;
    font-family: "Inter", "Helvetica Neue", Arial, sans-serif;
    color: var(--white);
  }
  .quadrant { position: absolute; width: 400px; height: 600px; }
  .quadrant--purple { left: 0; top: 0; background: var(--purple); }
  .quadrant--orange { left: 400px; top: 0; background: var(--orange); }
  .quadrant--blue { left: 0; top: 598px; height: 602px; background: var(--blue); }
  .quadrant--pink { left: 400px; top: 598px; height: 602px; background: var(--pink); }

  .illustration-area {
    position: absolute;
    left: 0; top: 123px;
    width: 800px; height: 777px;
    background: linear-gradient(180deg,
      rgba(255, 214, 40, 0.16) 0%,
      rgba(214, 16, 138, 0.14) 50%,
      rgba(26, 184, 238, 0.12) 100%);
  }

  .brand-bar {
    position: absolute;
    left: 207px; top: 0;
    width: 386px; height: 123px;
    background: var(--charcoal);
    display: flex;
    align-items: center;
    justify-content: center;
    gap: 14px;
  }
  .brand-bar__mark { width: 34px; height: 34px; background: var(--white); }
  .brand-bar__name {
    font-weight: 700;
    text-transform: uppercase;
    color: var(--white);
    line-height: 1.05;
    margin: 0;
  }
  .brand-bar__name span { display: block; }
  .brand-bar__name .brand-bar__primary { font-size: 29px; letter-spacing: 3px; }
  .brand-bar__name .brand-bar__secondary { font-size: 11px; letter-spacing: 3.2px; }

  .headline {
    position: absolute;
    left: 0; top: 170px;
    width: 800px;
    margin: 0;
    text-align: center;
    font-weight: 700;
    font-size: 80px;
    line-height: 80px;
    letter-spacing: -2.8px;
    text-shadow: 3px 4px 6px var(--shadow);
  }
  .purpose {
    position: absolute;
    left: 0; top: 364px;
    width: 800px;
    margin: 0;
    text-align: center;
    font-weight: 700;
    font-size: 36px;
    line-height: 45.5px;
    letter-spacing: -1.3px;
    text-shadow: 2px 3px 5px var(--shadow);
  }
  .motto {
    position: absolute;
    left: -14px; top: 772px;
    margin: 0;
    font-weight: 700;
    font-size: 232px;
    line-height: 168px;
    letter-spacing: -8px;
    color: var(--headline-pink);
    opacity: 0.93;
    white-space: nowrap;
  }
  .motto span { display: block; }
  .motto .motto__second { margin-left: -28px; }
  .web-address {
    position: absolute;
    left: 0; top: 1140px;
    width: 800px;
    text-align: center;
    font-weight: 700;
    font-size: 20px;
    letter-spacing: -0.5px;
    color: var(--white);
  }
</style>
</head>
<body>
<main class="poster">
  <div class="quadrant quadrant--purple"></div>
  <div class="quadrant quadrant--orange"></div>
  <div class="quadrant quadrant--blue"></div>
  <div class="quadrant quadrant--pink"></div>

  <div class="illustration-area" role="img"
       aria-label="Background illustration: a head in profile, an anatomical heart and a star in overlapping bright tones"></div>

  <header class="brand-bar">
    <div class="brand-bar__mark"></div>
    <p class="brand-bar__name">
      <span class="brand-bar__primary">Larkmoor</span>
      <span class="brand-bar__secondary">Property Management</span>
    </p>
  </header>

  <h1 class="headline">Why do I come<br>to work?</h1>

  <p class="purpose">To feel fulfilled<br>by empathizing,<br>educating and<br>empowering<br>our clients<br>and co-workers<br>so that we can<br>build strong,<br>impactful<br>relationships</p>

  <p class="motto"><span class="motto__first">Own the</span><span class="motto__second">outcome</span></p>

  <footer class="web-address">www.larkmoorpm.example</footer>
</main>
</body>
</html>
```